Package Design for 15 lines of Tea

I need design variations for 15 different Tea lines.
The tea will be packaged in Tin cylinders.
I have attached several pictures to show you an example of the display we are modelling after along with other references.
The 15 tea lines are:
Scholar Leaf
Ingredients: Brazilian Mate, Mint
Energy Boost Tea
Ingredients: Yunnan Coffee, Dark Puer
Relaxation Tea
Ingredients: Lotus Flower, South African Rooibos
Beauty Tea
Ingredients: Rose, Chrysanthemum, Red Dates, Huangqi
Sore Throat Tea
Ingredients: Honeysuckle, Pang Da Hai, Chamomile, Licorice Root
Get Well Tea
Ingredients: Ginger, Rooibos, Orange peel, Chinese Angelica
Diet Tea
Ingredients: Puer, Hibiscus, Lemongrass, Lotus Plumule
Bedtime Tea
Ingredients: Apple, Orange, Chamomile
South African Rooibos Tea
(pure)
Brazilian Yerba Mate Tea
(pure)
Long Jing Green Tea
(pure)
Darjeeling Black Tea
(pure)
Nepal Golden Tea
(Pure)
Bai Mu Dan White Tea
(pure)
Phoenix Oolong Tea
(pure)
Every Tea Blend should have three unique symbols that describe the purpose and theme of the blend. (!!Please don't make specific reference to the ingredients of the blends because some of these ingredients may be changed later. Stick to focusing on the intended purpose of the tea blend!!)
I would like the symbols to keep the same brushlike style that is consistent with our company logo.
Please keep the three block structure. I suggest keeping to just one color per tea blend. This will help each blend stand out between one another. I have a sample of the "Diet Tea" attached that I did myself to give you an idea of the structure I'm looking for, but obviously it's just my amateur version. Hope you can make them look far more appealing.
The ultimate goal is to build a picture language unique to our brand. As more products are released, we intend to potentially have hundreds of symbols, each with it's own meaning. So it would be nice when you present your pictures if you explain its intended meaning or message.
Deminsions:
Cylinder type 1: 82mm*38mmH
circular labels (along with your design) will be placed on the cap of product, and then the cylinder will be slanted on it's side to display the cap towards the customer.
Cylinder type 2: 65mm*152mmH
the labels will be placed on the side of the cylinder. In this version, try lining the three symbols in a vertical position. If this looks awful to you then feel free to go back to the horizontal style, but it would be nice to see what the vertical version looks like for reference.
Updates
Due to the scope of this project, please take note that I just increased my budget an additional 500 dollars more.
I also just added a 100 dollar second place prize. Don't want to see hard work unrewarded.
Feel free to send a few samples and I will provide prompt feedback. Please don't feel that you must submit all 15 lines at the same time.
Project Deadline Extended
Reason: I am extending the deadline as I feel there are more detailed revisions that need to be made until final selection.
Target Market(s)
Middle to Upper Class Consumers in China
Industry/Entity Type
It Company
Other font styles liked:
- font similar to font on company logo
Requirements
Must have
- Tea Designs must be in harmony with company logo and theme.
Should not have
- Avoid using Chinese characters as symbols. They may seem cool to westerners, but it's tacky for Chinese consumers.

```html
<!DOCTYPE html>
<html lang="en">
<head>
<meta charset="utf-8">
<title>Scholar Leaf – Cap Label</title>
<link rel="stylesheet" href="https://fonts.googleapis.com/css2?family=Special+Elite&display=swap">
<style>
  :root {
    --ink: #2b2a29;
    --mint: #a5d4c0;
    --page: #ffffff;
  }
  html, body {
    margin: 0;
    padding: 0;
    width: 1200px;
    height: 1200px;
    overflow: hidden;
    background: var(--page);
  }
  .cap-label {
    display: block;
    width: 1200px;
    height: 1200px;
  }
  .label-rim { fill: var(--ink); }
  .label-field { fill: var(--mint); }
  .symbol-column { fill: var(--ink); }
  .column-gap { fill: var(--mint); }
  .block-text {
    font-family: "Special Elite", "Courier New", monospace;
    fill: var(--mint);
  }
  .line-name {
    font-family: "Special Elite", "Courier New", monospace;
    fill: var(--ink);
    font-size: 50px;
  }
  .ingredients {
    font-family: "Special Elite", "Courier New", monospace;
    fill: var(--ink);
    font-size: 70px;
  }
</style>
</head>
<body>
<svg class="cap-label" viewBox="0 0 1200 1200" xmlns="http://www.w3.org/2000/svg">
  <defs>
    <clipPath id="field-clip">
      <circle cx="600" cy="600" r="555"/>
    </clipPath>
    <linearGradient id="symbol-tone" x1="0" y1="0" x2="1" y2="1">
      <stop offset="0" stop-color="#3a4a44"/>
      <stop offset="1" stop-color="#5f8677"/>
    </linearGradient>
  </defs>

  <circle class="label-rim" cx="600" cy="600" r="598"/>
  <circle class="label-field" cx="600" cy="600" r="555"/>

  <g class="symbol-stack" clip-path="url(#field-clip)">
    <rect class="symbol-column" x="468" y="0" width="263" height="1200"/>
    <rect class="column-gap" x="468" y="396" width="263" height="27"/>
    <rect class="column-gap" x="468" y="786" width="263" height="31"/>
  </g>

  <text class="block-text block-numbers" x="600" y="264" text-anchor="middle" font-size="124">123</text>

  <rect class="block-symbol" x="482" y="495" width="230" height="230" rx="18"
        fill="url(#symbol-tone)" role="img"
        aria-label="Brush-style symbol of a closed book, drawn in mint lines"/>

  <text class="block-text block-letters" x="600" y="1042" text-anchor="middle" font-size="118">abc</text>

  <text class="line-name" x="262" y="618" text-anchor="middle">Scholar Leaf</text>

  <text class="ingredients" transform="translate(912 210) rotate(90)"
        textLength="712" lengthAdjust="spacingAndGlyphs">Brazilian Mate, Mint</text>
</svg>
</body>
</html>
```